Adept Corvana Recruitment company

We require a website for job recruitment company called "Adept Corvana"
Our company is specialising in recruitment of skilled labour from Sri Lanka into Australian market.
We would like to include a job advertising plugin where jobs can be listed and applied for .
COPYWRITING MUST BE INCLUDED !

Industry/Entity Type

Recruitment

Coding

Coded - Design and coding required

Number of Pages Required

5+ page

Colors

Designer to choose colors to be used in the design.

```html
<!DOCTYPE html>
<html lang="en">
<head>
<meta charset="utf-8">
<title>Adept Corvana — Find Your Perfect Job Match</title>
<link href="https://fonts.googleapis.com/css2?family=Poppins:wght@400;500;600;700;800&display=swap" rel="stylesheet">
<style>
:root{
  --blue:#0b4ea2;
  --blue-dark:#083c80;
  --ink:#111111;
  --text:#333333;
  --muted:#666666;
  --grey-band:#e9e9e9;
  --card:#ffffff;
  --chip:#e4e4e4;
  --footer:#1c1c1c;
  --line:#d6d6d6;
}
*{box-sizing:border-box;margin:0;padding:0}
html,body{width:1200px;height:4284px;overflow:hidden}
body{font-family:"Poppins",sans-serif;color:var(--text);background:#fff;position:relative}
a{color:inherit;text-decoration:none}

/* header */
.brand{position:absolute;left:88px;top:26px;font-weight:700;font-size:30px;line-height:34px;color:var(--ink)}
.brand small{display:block;font-size:22px;line-height:24px;color:var(--blue);padding-left:44px}
.nav{position:absolute;left:456px;top:44px;display:flex;gap:40px;font-size:16px;color:var(--ink);z-index:2}
.nav .active{color:var(--blue)}
.btn{display:inline-flex;align-items:center;justify-content:center;background:var(--blue);color:#fff;font-weight:500;border-radius:4px}
.contact-btn{position:absolute;left:984px;top:32px;width:128px;height:46px;font-size:16px;z-index:2}

/* hero */
.hero-photo{position:absolute;left:600px;top:0;width:600px;height:700px;background:linear-gradient(160deg,#e8ecef 0%,#b9c1c8 35%,#5a5f66 70%,#33373d 100%)}
.hero-title{position:absolute;left:88px;top:204px;font-size:60px;line-height:64px;font-weight:800;color:var(--ink);letter-spacing:.5px}
.hero-sub{position:absolute;left:88px;top:436px;font-size:15px;font-weight:600;color:var(--ink)}
.search{position:absolute;left:88px;top:500px;width:624px;height:64px;background:#fff;border-radius:6px;box-shadow:0 4px 18px rgba(0,0,0,.12);display:flex;align-items:center;padding:0 10px;gap:12px}
.search .field{flex:1;height:42px;border:1px solid var(--line);border-radius:4px;display:flex;align-items:center;gap:10px;padding:0 14px;font-size:13px;color:#999}
.search .btn{width:120px;height:42px;font-size:15px}
.cand{position:absolute;left:100px;top:612px;display:flex;align-items:center;gap:10px}
.cand-txt{font-size:14px;font-weight:700;color:var(--ink);line-height:16px}
.cand-txt span{display:block;font-size:10px;font-weight:400;color:var(--muted)}
.avatars{display:flex}
.avatars i{width:28px;height:28px;border-radius:50%;border:2px solid #fff;background:linear-gradient(#8a8f96,#4a4f57);margin-left:-8px}

.stats{position:absolute;left:88px;top:696px;width:1024px;height:152px;background:var(--blue);border-radius:8px;display:flex;justify-content:space-around;align-items:center;padding:0 40px}
.stat{display:flex;align-items:center;gap:18px;color:#fff}
.stat .ico{width:62px;height:62px;background:#fff;border-radius:6px;display:flex;align-items:center;justify-content:center}
.stat b{display:block;font-size:26px;line-height:30px;font-weight:700}
.stat span{font-size:15px}

/* about */
.about-back{position:absolute;left:200px;top:938px;width:330px;height:280px;background:linear-gradient(140deg,#cfd6dc,#7b8590);border-radius:4px}
.about-front{position:absolute;left:292px;top:1052px;width:290px;height:270px;background:linear-gradient(160deg,#dfe3e6,#8e969e 60%,#3d434a);border:6px solid #fff;box-shadow:0 6px 18px rgba(0,0,0,.15)}
.about-text{position:absolute;left:628px;top:978px;width:480px}
.h2{font-size:38px;font-weight:700;color:var(--ink);line-height:46px}
.p{font-size:14px;line-height:20px;color:var(--text)}
.about-text .p{margin-top:10px}
.about-text .btn{margin-top:22px;width:112px;height:42px;font-size:14px}

/* how it works */
.how{position:absolute;left:0;top:1420px;width:1200px;height:560px;background:var(--grey-band)}
.center-title{position:absolute;left:0;width:1200px;text-align:center}
.step{position:absolute;top:148px;width:328px;height:336px;text-align:center;padding-top:36px}
.step.featured{background:#fff;border-radius:6px;box-shadow:0 6px 24px rgba(0,0,0,.12);height:344px;z-index:1}
.step.plain{background:#ececec;border-radius:6px}
.step h3{font-size:16px;font-weight:600;color:var(--ink);margin-top:14px}
.step .p{width:260px;margin:8px auto 0;font-size:13px;line-height:19px}
.more{display:inline-block;margin-top:16px;font-size:13px;font-weight:500;color:var(--blue)}

/* industries */
.ind-sub{position:absolute;left:390px;top:2128px;width:420px;text-align:center}
.chips{position:absolute;left:160px;top:2192px;width:880px;display:grid;grid-template-columns:repeat(3,272px);gap:28px 32px}
.chip{height:72px;background:var(--chip);border-radius:4px;display:flex;align-items:center;justify-content:center;gap:14px;font-size:15px;font-weight:500;color:#444;text-transform:uppercase}
.chip.on{background:var(--blue);color:#fff}
.view-btn{position:absolute;left:540px;top:2410px;width:120px;height:42px;font-size:14px}

/* team */
.team{position:absolute;left:0;top:2528px;width:1200px;height:512px;background:var(--grey-band);overflow:hidden}
.team-sub{position:absolute;left:390px;top:108px;width:420px;text-align:center}
.team-card{position:absolute;top:184px;width:380px;height:196px;background:#fff;border-radius:6px;box-shadow:0 4px 16px rgba(0,0,0,.08);padding:24px}
.team-card.mid{border:2px solid var(--blue)}
.face{position:absolute;left:24px;top:30px;width:140px;height:140px;border-radius:4px}
.team-info{position:absolute;left:184px;top:28px;right:20px}
.team-info h4{font-size:16px;font-weight:600;color:var(--ink)}
.team-info em{display:block;font-style:normal;font-size:11px;color:var(--muted)}
.team-info .p{font-size:12px;line-height:17px;margin-top:8px}
.team-info .row{display:flex;justify-content:space-between;align-items:center;margin-top:10px;font-size:12px;color:var(--blue);font-weight:500}
.dots{position:absolute;left:560px;top:436px;display:flex;gap:14px;align-items:center}
.dots i{width:12px;height:12px;border-radius:50%;background:#b8c6da}
.dots i.on{width:22px;height:22px;background:var(--blue);border:4px solid #cfdcef}

/* news */
.news-sub{position:absolute;left:390px;top:3180px;width:420px;text-align:center}
.news-card{position:absolute;top:3248px;width:304px;height:504px;background:#fff;border-radius:6px;box-shadow:0 4px 18px rgba(0,0,0,.1);text-align:center;overflow:hidden}
.news-card.mid{border:2px solid var(--blue);box-shadow:0 8px 24px rgba(11,78,162,.25)}
.news-img{height:258px;margin:10px;border-radius:2px;position:relative}
.date{position:absolute;left:0;top:0;background:var(--blue);color:#fff;font-size:12px;padding:4px 12px}
.news-card h3{font-size:17px;font-weight:600;color:var(--ink);margin-top:22px;text-transform:uppercase}
.news-card .p{width:256px;margin:10px auto 0;font-size:12px;line-height:18px}
.arrow-btn{position:absolute;top:3398px;width:36px;height:36px;border-radius:50%;background:#d9d9d9;display:flex;align-items:center;justify-content:center}

/* newsletter */
.newsletter{position:absolute;left:0;top:3800px;width:1200px;height:100px;background:var(--blue)}
.newsletter h3{position:absolute;left:92px;top:34px;font-size:26px;font-weight:700;color:#fff}
.nl-input{position:absolute;left:576px;top:32px;width:392px;height:40px;background:#fff;font-size:13px;color:#999;padding:10px 14px}
.nl-btn{position:absolute;left:968px;top:32px;width:136px;height:40px;background:#111;color:#fff;font-size:14px;font-weight:700;display:flex;align-items:center;justify-content:center}

/* footer */
.footer{position:absolute;left:0;top:3900px;width:1200px;height:384px;background:var(--footer);color:#e6e6e6}
.f-brand{position:absolute;left:92px;top:40px;font-weight:700;font-size:40px;line-height:42px;color:#fff}
.f-brand small{display:block;font-size:28px;line-height:30px;color:#4f8fe0;padding-left:58px}
.f-about{position:absolute;left:92px;top:158px;width:260px;font-size:13px;line-height:19px;color:#cfcfcf}
.f-col{position:absolute;top:76px}
.f-col h5{font-size:16px;font-weight:600;color:#fff;margin-bottom:16px}
.f-col li{list-style:none;font-size:14px;line-height:30px;color:#d4d4d4}
.f-info li{display:flex;gap:12px;align-items:flex-start;line-height:20px;margin-bottom:14px}
.f-info span{font-size:13px}
.copy{position:absolute;left:0;bottom:20px;width:1200px;text-align:center;font-size:12px;color:#aaa}
</style>
</head>
<body>

<!-- Header -->
<div class="hero-photo" role="img" aria-label="Photo of three business people in suits reviewing work at a laptop in an office"></div>
<div class="brand">Adept<small>Corvana</small></div>
<nav class="nav"><a class="active">Home</a><a>About Us</a><a>Employee</a><a>Candidates</a><a>Blog</a></nav>
<a class="btn contact-btn">Contact Us</a>

<!-- Hero -->
<h1 class="hero-title">FIND YOUR<br>PERFECT JOB<br>MATCH</h1>
<p class="hero-sub">Find Jobs, Employment &amp; Career Opportunities</p>
<div class="search">
  <div class="field"><svg width="14" height="14" viewBox="0 0 14 14"><circle cx="6" cy="6" r="4.5" fill="none" stroke="#999" stroke-width="1.5"/><path d="M9.5 9.5L13 13" stroke="#999" stroke-width="1.5"/></svg>Job Title</div>
  <div class="field"><svg width="12" height="14" viewBox="0 0 12 14"><path d="M6 13S1 8 1 5a5 5 0 0 1 10 0c0 3-5 8-5 8z" fill="none" stroke="#999" stroke-width="1.4"/><circle cx="6" cy="5" r="1.6" fill="#999"/></svg>Location</div>
  <a class="btn">Search</a>
</div>
<div class="cand">
  <div class="cand-txt">50k+<span>Candidates</span></div>
  <div class="avatars" role="img" aria-label="Small round candidate portraits"><i></i><i></i><i></i><i></i><i></i></div>
</div>

<div class="stats">
  <div class="stat"><div class="ico"><svg width="30" height="28" viewBox="0 0 30 28"><rect x="2" y="8" width="26" height="18" rx="2" fill="#0b4ea2"/><rect x="10" y="2" width="10" height="7" rx="1" fill="none" stroke="#0b4ea2" stroke-width="2.4"/></svg></div><div><b>50K+</b><span>Job Vacancy</span></div></div>
  <div class="stat"><div class="ico"><svg width="32" height="28" viewBox="0 0 32 28"><circle cx="10" cy="8" r="5" fill="#0b4ea2"/><circle cx="22" cy="8" r="5" fill="#0b4ea2"/><path d="M1 26a9 9 0 0 1 18 0zM13 26a9 9 0 0 1 18 0z" fill="#0b4ea2"/></svg></div><div><b>50K+</b><span>People Got Hire</span></div></div>
  <div class="stat"><div class="ico"><svg width="26" height="30" viewBox="0 0 26 30"><rect x="2" y="2" width="22" height="27" fill="#0b4ea2"/><g fill="#fff"><rect x="6" y="6" width="4" height="4"/><rect x="16" y="6" width="4" height="4"/><rect x="6" y="13" width="4" height="4"/><rect x="16" y="13" width="4" height="4"/><rect x="10" y="21" width="6" height="8"/></g></svg></div><div><b>50K+</b><span>Companies</span></div></div>
</div>

<!-- About -->
<div class="about-back" role="img" aria-label="Photo of colleagues at a meeting table"></div>
<div class="about-front" role="img" aria-label="Photo of a smiling professional team standing together"></div>
<div class="about-text">
  <h2 class="h2">ABOUT US</h2>
  <p class="p">Adept Corvana connects skilled tradespeople and professionals from Sri Lanka with trusted employers across Australia. We handle screening, skills checks, visa guidance and relocation support, so every placement starts strong.</p>
  <p class="p">From Colombo to Sydney, our team stays beside candidates and employers at every step.</p>
  <a class="btn">Read More</a>
</div>

<!-- How it works -->
<section class="how">
  <h2 class="h2 center-title" style="top:70px">SEE HOW IT WORKS</h2>
  <div class="step plain" style="left:100px">
    <svg width="48" height="48" viewBox="0 0 48 48"><rect x="10" y="4" width="28" height="38" rx="2" fill="none" stroke="#222" stroke-width="2.4"/><circle cx="24" cy="16" r="5" fill="none" stroke="#222" stroke-width="2.2"/><path d="M16 30a8 8 0 0 1 16 0" fill="none" stroke="#222" stroke-width="2.2"/><circle cx="36" cy="38" r="7" fill="#fff" stroke="#222" stroke-width="2.2"/><path d="M33 38l2 2 4-4" stroke="#222" stroke-width="2" fill="none"/></svg>
    <h3>REGISTER PROFILE</h3>
    <p class="p">Create your free profile, upload your CV and list the trade skills you bring.</p>
    <a class="more">Read More</a>
  </div>
  <div class="step featured" style="left:436px">
    <svg width="52" height="48" viewBox="0 0 52 48"><rect x="6" y="12" width="40" height="24" rx="4" fill="none" stroke="#0b4ea2" stroke-width="2.4"/><circle cx="18" cy="24" r="5" fill="none" stroke="#0b4ea2" stroke-width="2.2"/><path d="M23 24h16v5M33 24v4" stroke="#0b4ea2" stroke-width="2.2" fill="none"/></svg>
    <h3>SEARCH YOUR JOB</h3>
    <p class="p">Browse verified Australian roles by trade, region, pay and visa pathway.</p>
    <a class="more">Read More</a>
  </div>
  <div class="step plain" style="left:772px">
    <svg width="48" height="48" viewBox="0 0 48 48"><rect x="10" y="4" width="28" height="40" rx="2" fill="none" stroke="#222" stroke-width="2.4"/><circle cx="24" cy="16" r="5" fill="none" stroke="#222" stroke-width="2.2"/><path d="M16 30a8 8 0 0 1 16 0M16 36h16" fill="none" stroke="#222" stroke-width="2.2"/></svg>
    <h3>APPLY FOR JOB</h3>
    <p class="p">Apply in one click and our consultants guide you through interviews and visas.</p>
    <a class="more">Read More</a>
  </div>
</section>

<!-- Industries -->
<h2 class="h2 center-title" style="top:2062px">INDUSTRIES HIRING</h2>
<p class="p ind-sub">Australian employers are hiring skilled Sri Lankan talent across these sectors now.</p>
<div class="chips">
  <div class="chip"><svg width="24" height="22" viewBox="0 0 24 22"><rect x="1" y="1" width="22" height="15" rx="1" fill="none" stroke="#444" stroke-width="2"/><path d="M8 21h8M12 16v5" stroke="#444" stroke-width="2"/></svg>IT Support</div>
  <div class="chip on"><svg width="24" height="22" viewBox="0 0 24 22"><path d="M2 20L9 12l5 4 8-12" stroke="#fff" stroke-width="2.4" fill="none"/></svg>Digital Marketing</div>
  <div class="chip"><svg width="26" height="22" viewBox="0 0 26 22"><path d="M13 2v18M5 20h16M3 6h20M6 6l-4 8h8zM20 6l-4 8h8z" stroke="#444" stroke-width="1.8" fill="none"/></svg>Lawyer</div>
  <div class="chip"><svg width="20" height="24" viewBox="0 0 20 24"><rect x="1" y="1" width="18" height="22" rx="2" fill="none" stroke="#444" stroke-width="2"/><rect x="4" y="4" width="12" height="5" fill="#444"/><g fill="#444"><rect x="4" y="12" width="3" height="3"/><rect x="9" y="12" width="3" height="3"/><rect x="14" y="12" width="3" height="3"/><rect x="4" y="17" width="3" height="3"/><rect x="9" y="17" width="3" height="3"/><rect x="14" y="17" width="3" height="3"/></g></svg>Accountant</div>
  <div class="chip"><svg width="24" height="24" viewBox="0 0 24 24"><path d="M3 21l3-8L17 2l5 5L11 18z" stroke="#444" stroke-width="2" fill="none"/></svg>Graphic Designer</div>
  <div class="chip"><svg width="26" height="22" viewBox="0 0 26 22"><rect x="8" y="1" width="17" height="12" fill="none" stroke="#444" stroke-width="2"/><circle cx="5" cy="9" r="3" fill="#444"/><path d="M0 21a5 5 0 0 1 10 0z" fill="#444"/></svg>Teacher</div>
</div>
<a class="btn view-btn">View More</a>

<!-- Team -->
<section class="team">
  <h2 class="h2 center-title" style="top:50px">OUR TEAM</h2>
  <p class="p team-sub">Meet the consultants who bridge Sri Lanka and Australia for every candidate.</p>
  <div class="team-card" style="left:-70px">
    <div class="face" style="background:linear-gradient(#d8dce0,#8f98a2)" role="img" aria-label="Portrait of team member Ravin Perera"></div>
    <div class="team-info"><h4>RAVIN PERERA</h4><em>Founder &amp; CEO</em><p class="p">Guides candidates from their first interview to day one on site.</p><div class="row"><span>Read More</span><span>→</span></div></div>
  </div>
  <div class="team-card mid" style="left:388px">
    <div class="face" style="background:linear-gradient(#e4e6e8,#a3a9b0)" role="img" aria-label="Portrait of team member Owen Hartley"></div>
    <div class="team-info"><h4>OWEN HARTLEY</h4><em>Placement Lead</em><p class="p">Partners with Australian employers to match roles with proven skills.</p><div class="row"><span>Read More</span><span>→</span></div></div>
  </div>
  <div class="team-card" style="left:808px">
    <div class="face" style="background:linear-gradient(#f1c24a,#d9a126)" role="img" aria-label="Portrait of team member Nimal Fonseka"></div>
    <div class="team-info"><h4>NIMAL FONSEKA</h4><em>Visa Advisor</em><p class="p">Keeps every visa file accurate, complete and moving on time.</p><div class="row"><span>Read More</span><span>→</span></div></div>
  </div>
  <div class="dots"><i></i><i class="on"></i><i></i></div>
</section>

<!-- News -->
<h2 class="h2 center-title" style="top:3124px">RECENT NEWS ARTICLES</h2>
<p class="p news-sub">Insights on hiring, visas and working life for Sri Lankans in Australia.</p>
<div class="arrow-btn" style="left:42px"><svg width="10" height="14" viewBox="0 0 10 14"><path d="M8 1L2 7l6 6" stroke="#333" stroke-width="2" fill="none"/></svg></div>
<div class="arrow-btn" style="left:1124px"><svg width="10" height="14" viewBox="0 0 10 14"><path d="M2 1l6 6-6 6" stroke="#333" stroke-width="2" fill="none"/></svg></div>
<article class="news-card" style="left:96px">
  <div class="news-img" style="background:linear-gradient(150deg,#8a6a4a,#3a2c22)" role="img" aria-label="Photo of a business meeting at a desk"><span class="date">April/26/2022</span></div>
  <h3>Attract Sales</h3><p class="p">How skilled Sri Lankan staff help Australian businesses grow sales, fill shifts and serve customers better.</p><a class="more">Read More</a>
</article>
<article class="news-card mid" style="left:440px">
  <div class="news-img" style="background:linear-gradient(150deg,#2a5a9a,#0e2a55)" role="img" aria-label="Photo of hands typing on a laptop with glowing data"><span class="date">April/26/2022</span></div>
  <h3>Potential Employers</h3><p class="p">Which Australian sectors are hiring overseas talent this year, and what they look for in a CV.</p><a class="more">Read More</a>
</article>
<article class="news-card" style="left:792px">
  <div class="news-img" style="background:linear-gradient(150deg,#c9d3dd,#6f7d8c)" role="img" aria-label="Photo of a laptop showing a job listings website"><span class="date">April/26/2022</span></div>
  <h3>Attract Profits</h3><p class="p">Why sponsoring proven tradespeople cuts turnover, lowers training costs and lifts long-term profit.</p><a class="more">Read More</a>
</article>

<!-- Newsletter -->
<section class="newsletter">
  <h3>SUBSCRIBE NEWSLETTER</h3>
  <div class="nl-input">Enter Your Email</div>
  <div class="nl-btn">SUBSCRIBE</div>
</section>

<!-- Footer -->
<footer class="footer">
  <div class="f-brand">Adept<small>Corvana</small></div>
  <p class="f-about">Recruiting skilled Sri Lankan talent for trusted Australian employers.</p>
  <div class="f-col" style="left:528px"><h5>QUICK LINK</h5><ul><li>Home</li><li>About Us</li><li>Categories</li><li>Team</li><li>Blog</li></ul></div>
  <div class="f-col" style="left:712px"><h5>SUPPORT</h5><ul><li>Privacy Center</li><li>Security Center</li><li>Contact Us</li><li>Terms &amp; Conditions</li></ul></div>
  <div class="f-col f-info" style="left:944px"><h5>INFORMATION</h5><ul>
    <li><svg width="16" height="14" viewBox="0 0 16 14"><rect x="1" y="1" width="14" height="12" fill="none" stroke="#4f8fe0" stroke-width="1.6"/><path d="M1 2l7 6 7-6" stroke="#4f8fe0" stroke-width="1.6" fill="none"/></svg><span>hello@adeptcorvana.example</span></li>
    <li><svg width="14" height="16" viewBox="0 0 14 16"><path d="M7 15S1 9 1 6a6 6 0 0 1 12 0c0 3-6 9-6 9z" fill="#4f8fe0"/><circle cx="7" cy="6" r="2" fill="#1c1c1c"/></svg><span>14 Harbourline Road,<br>Kelston NSW 2190</span></li>
    <li><svg width="14" height="14" viewBox="0 0 14 14"><path d="M3 1l3 3-2 2a9 9 0 0 0 4 4l2-2 3 3-2 2C5 13 1 9 1 3z" fill="#4f8fe0"/></svg><span>(02) 5550 0148</span></li>
  </ul></div>
  <p class="copy">© Copyright 2022 Adept Corvana. All Rights Reserved</p>
</footer>

</body>
</html>
```